My Professional Resume/CV Design

Hi Pixel Harbor experts, I need a professional resume/CV design for using my carrier hiring activities. I have a draft and this draft is 2 types.
1) Traditional IT Major Company Senior(Manager Level) to Director level application (File: Tanabe_Emiko_Res_EN2023AprA)
>Application example companies: Velmora, Drakt, Quindle, Brightmarsh, HoltenWare, Fenwick Ridge, Zentravix, Morivon, Quorexa, Plinth, dZop, Kelvarna etc
>This should not be fancy. Please make format with traditional/gentle/standard but also need to appear unique point such as icons, borderlines etc
2) Cutting-Edge (Web 3.0/metaverse/NFT/Crypto) Start-up or Young (Less 5 year's history) Company Director and C-Levels position application (Tanabe_Emiko_Res_EN2023Apr_typeC)
>Application Example Companies: Tessaluk Studios, Vorlexa, Zintaro.example, Wovenpath, Lumbrook, FernPocket, Thaxel, Kipa/Dult/Snov, Morvik, QUESTAN, wordLYM etc
>This resume format should be something "edge" "advanced" "future" and "high-tech", so need to your high sense of design technics.
Both drafts is without a profile picture, but I need to put in my portfolio picture (Just attached one is my 2018's, you can trim and edit as well)
For the document format, please send me to WORD and PAGES both. and total MAX 2 page in all contents please (No more 3 pages)
Target Market(s)
Traditional Major Tech Company's VP/Directors or/and Latest Web 3.0 StartUp C-Levels (CEO/CTO/CSO/COO etc)
Industry/Entity Type
Technology
Font styles to use
Other font styles liked:
- Choose 3 a)Century Gothic b) Avenir c)Graphik d)Kohinoor e)Optima f)Platino
Look and feel
Each slider illustrates characteristics of the customer's brand and the style your logo design should communicate.

```html
<!DOCTYPE html>
<html lang="en">
<head>
<meta charset="utf-8">
<title>Emiko Tanabe – Curriculum Vitae</title>
<link href="https://fonts.googleapis.com/css2?family=Montserrat:wght@400;500;600;700;800&display=swap" rel="stylesheet">
<style>
:root{
  --backdrop:#dedfe1;
  --paper:#ffffff;
  --ink:#1d1d1f;
  --ink-soft:#3a3a3e;
  --tint:#f6e8f5;
  --tint-grey:#f3f3f4;
  --rule:#d9c7d8;
  --rule-dark:#222;
}
*{box-sizing:border-box;margin:0;padding:0}
html,body{width:1200px;height:591px;overflow:hidden}
body{background:var(--backdrop);font-family:"Montserrat",sans-serif;color:var(--ink);position:relative}
.page{position:absolute;top:53px;width:341px;height:483px;background:var(--paper);overflow:hidden;box-shadow:0 4px 8px rgba(0,0,0,.12)}
.page--one{left:57px}.page--two{left:429px}.page--three{left:802px}
.masthead{position:absolute;left:18px;right:18px;top:17px}
.masthead__label{font-size:8.3px;font-weight:400;letter-spacing:.1px;padding-bottom:3px;border-bottom:.6px solid var(--rule)}
.masthead__name{font-size:16.5px;font-weight:800;letter-spacing:.2px;margin-top:2px;line-height:1.1}
.masthead__city{font-size:7.3px;font-weight:400;letter-spacing:0;margin-left:2px}
.body{position:absolute;left:18px;right:18px;font-size:3.95px;line-height:6.6px;color:var(--ink-soft)}
p{margin:0}
.role{display:flex;justify-content:space-between;background:var(--tint);padding:1.6px 4px;font-size:4.1px;line-height:6px;color:var(--ink);margin:4px 0 5px}
.text{padding:0 2px}
.list{list-style:none;padding:0 2px;margin-top:2px}
.list li{padding-left:3px;text-indent:-3px}
.list li::before{content:"· "}
.note{font-weight:600;color:var(--ink);padding:0 2px;margin-top:1px}
.section-title{font-size:7.4px;font-weight:500;color:var(--ink);padding-bottom:3px;border-bottom:.6px solid var(--rule);margin-bottom:3px;letter-spacing:.1px;line-height:9px}
.footer{position:absolute;left:18px;right:18px;top:463px;border-top:.6px solid var(--rule);padding-top:3px;text-align:center;font-size:4.4px;letter-spacing:1.4px;color:var(--ink)}
.footer span{margin:0 9px}
/* page one */
.intro-band{position:absolute;left:78px;right:0;top:55px;height:87px;background:var(--tint)}
.portrait-ring{position:absolute;left:12px;top:56px;width:88px;height:88px;border-radius:50%;background:var(--tint);border:1px solid #efdcee}
.portrait{position:absolute;left:17px;top:61px;width:78px;height:78px;border-radius:50%;background:radial-gradient(circle at 50% 40%,#6f6368 0%,#2f2a2d 55%,#1b1a1c 100%)}
.intro{position:absolute;left:108px;right:18px;top:60px}
.intro__title{font-size:5.6px;font-weight:700;color:var(--ink);padding-bottom:1.5px;border-bottom:.6px solid var(--rule-dark);margin-bottom:2px}
.intro__text{font-size:3.8px;line-height:4.8px;color:var(--ink);padding:0 2px;width:180px}
.path{margin-top:6px}
.path__row{display:flex;justify-content:space-between;font-size:3.6px;line-height:5.9px;color:var(--ink);padding:0 2px}
.headline{position:absolute;left:18px;right:18px;top:150px}
.headline__main{font-size:7px;font-weight:500;color:var(--ink);letter-spacing:-.1px;line-height:9px;white-space:nowrap}
.headline__sub{font-size:4.4px;line-height:6px;color:var(--ink);padding-left:2px;padding-bottom:3px;border-bottom:.6px solid var(--rule);white-space:nowrap}
.summary{top:171px;font-size:4.25px;line-height:6.3px;text-align:justify;padding:0 2px}
.education{top:243px}
.education__row{display:flex;justify-content:space-between;font-size:4.5px;line-height:6px;color:var(--ink);margin-top:3px}
.highlights{top:275px}
.highlight{background:var(--tint-grey);padding:2.5px 5px;margin-bottom:1.4px;font-size:3.85px;line-height:4.8px;color:var(--ink);height:15.6px;overflow:hidden}
.experience{top:387px}
.experience .text{font-size:3.9px;line-height:6.3px}
/* page three */
.competencies{display:grid;grid-template-columns:1fr 1fr 1fr;margin-top:6px}
.competencies ul{list-style:none;font-size:3.95px;line-height:6.6px;color:var(--ink)}
.competencies ul+ul{border-left:.6px solid var(--rule);padding-left:24px}
.competencies li::before{content:"· "}
</style>
</head>
<body>

<!-- Page 1 -->
<section class="page page--one">
  <header class="masthead">
    <p class="masthead__label">CURRICULUM VITAE</p>
    <h1 class="masthead__name">EMIKO TANABE <span class="masthead__city">(Wanchai, Hong Kong)</span></h1>
  </header>

  <div class="intro-band"></div>
  <div class="portrait-ring"></div>
  <div class="portrait" role="img" aria-label="Portrait photo of the candidate"></div>

  <div class="intro">
    <h2 class="intro__title">PROFILE</h2>
    <p class="intro__text">Seniorbusiness Leader, Strategist And Driver Of Change. Worked In Over 30 Countries Across 4 Continents.passion For Company Turnaround, Business Development And Growth.</p>
    <h2 class="intro__title path">CAREER PATH</h2>
    <div class="path__row"><span>Inside Renewals Sales | Kestrel Networks. | Hong Kong | Part Time</span><span>Jul 2022 - Present</span></div>
    <div class="path__row"><span>Guild Business Division Sales Operation Head | Voxelwork Japan | Hong Kong</span><span>Early 2022</span></div>
    <div class="path__row"><span>Business Development Manager | ORN HK Limited | Hong Kong</span><span>Apr 2021- Apr 2022</span></div>
    <div class="path__row"><span>Business Development| Manager Renza High-Tech (Hong Kong) Limited | Hong Kong</span><span>Aug 2020 – Apr 2021</span></div>
  </div>

  <div class="headline">
    <h2 class="headline__main">BUSINESS DEVELOPMENT | VENDOR MANAGEMENT | PARTNER CHANNEL SALES</h2>
    <p class="headline__sub">Web 3+ Technology &amp; Cyber Security / Strategic Planning &amp; Execution / Proposal &amp; Contract Management</p>
  </div>

  <p class="body summary">My value and career will only increase in a diverse and multinational work environment High-impact growth-oriented professional demonstrating a strong grasp of current marketing tools and strategies aligned with Cutting-edge technology with an interest in the transformation of society/era events within the industry and cyber security with an Entrepreneurial spirit. Strategically collaborate with external vendors and internal business partners; manages various commercial platforms, systems, domains, and channels to ensure scale marketing and lead development capabilities in line with business growth plans that deliver high-quality results. Participate in supply chain strategy development, developing implementation plans, and methods of dealing with business. Display strong analytical ability to evaluate end-to-end customer experience across multiple channels and customer touchpoints. Highly creative with experience in identifying target audiences and devising digital campaigns while valuing traditional methods that engage, inform, and motivate while staying abreast of industry trends. Conclude below 3 is my core abilities. “Cutting-Edge Technologies” “Business Development” and “Japan/APAC/Global Channel Sales”</p>

  <div class="body education">
    <h2 class="section-title">EDUCATION</h2>
    <div class="education__row"><span>Bachelor’s degree in economics/Philosophy</span><span>Eastgate University, Japan</span></div>
  </div>

  <div class="body highlights">
    <h2 class="section-title" style="margin-bottom:5px">HIGHLIGHTS OF QUALIFICATION</h2>
    <p class="highlight">· Expert levels of sense of abilities in conducting marketing research and analyzing data strategically to identify brand/product value propositions, prospect customers, markets, and major competitors</p>
    <p class="highlight">· Understands target audiences and competition dynamics with insights from various sources while leading integrated digital and offline marketing campaigns from concept to execution, on time and within scope and budget.</p>
    <p class="highlight">· Serve as supply chain interface for all major projects, with clear knowledge of project progress, logistics, and distribution development as well as implementation and execution of local and regional projects.</p>
    <p class="highlight">· Fluent in English and Japanese to communicate compelling value propositions for existing / prospective customers through different channels, digital/social communication, partnership, and sponsorship regularly and on a project basis.</p>
    <p class="highlight">· Conceptualize and develop brand/product sales plans and campaigns for companies and individual business lines, including planning, liaison, coordination, and execution.</p>
  </div>

  <div class="body experience">
    <h2 class="section-title" style="border:0;margin-bottom:0;padding-bottom:0">PROFESSIONAL EXPERIENCE</h2>
    <div class="role" style="margin-top:2px"><span>Inside Renewals Sales | Kestrel Networks. | Hong Kong | Part Time</span><span>Jul 2022 - Present</span></div>
    <p class="text">First visa-sponsored employee since the establishment of the APAC Hong Kong company (2017 and in total over 100+). Promotion to Territory Manager (Inside New Sales) is factored in. The agreement to start with renewal sales was to be able to build relationships with existing partners and to set the stage for the new position. Due to internal circumstances, there is no budgetary visibility for an Inside Sales Manager for the Japan Territory. Job hunting activity while still employed for reasons of wanting to advance own careers external, as prospects for promotion within the company are very low expectations by company reasons.</p>
  </div>

  <footer class="footer"><span>EMIKO TANABE</span>|<span>ETANABE512@MAIL.EXAMPLE</span>|<span>+852 0000 1234/0000 5678</span></footer>
</section>

<!-- Page 2 -->
<section class="page page--two">
  <header class="masthead">
    <p class="masthead__label">CURRICULUM VITAE</p>
    <h1 class="masthead__name">EMIKO TANABE <span class="masthead__city">(Wanchai, Hong Kong)</span></h1>
  </header>

  <div class="body" style="top:57px">
    <ul class="list" style="padding:0">
      <li>Distributor and Reseller (Partner) Management: Before I join, Kestrel was the low position for any of the partner’s sales, like quotation production due to only focused PO. I focusing what end users face on the problems and pain and shared with proper partners. A result, they never ask me for a quotation (they now can quote themself) and they proposed me to new sales plans and strategies. I just concentrated to do what my partner want and relationship development.</li>
      <li>Co-work with Territory Regional Team remotely: Mainly Japan Sales, SEs, CS, Technical Support</li>
      <li>Enhancing mutual synergies with other regional teams: Corporate team works with especially APAC another region team ( India/SEA/ANZ/China total 4 regions) and US and EMEA as well.</li>
    </ul>

    <div class="role"><span>Guild Business Division Sales Operation Head | Voxelwork Japan | Hong Kong</span><span>Early 2022</span></div>
    <p class="text">This entity is an NFT GameFi startup for “Play To Earn” players scholarship program. I joined as the authorized person under CEO. My role is a huge territory, from community management to design strategy and tactics for this scholarship business.</p>

    <div class="role"><span>Business Development Manager | ORN HK Limited | Hong Kong</span><span>Apr 2021- Apr 2022</span></div>
    <p class="text">Join from GM’s direct invitation due to he wanna survive the pandemic crisis, this is an IT reseller business provider in Hong Kong, China, SEA, and Japan market. Upon long-term mainly prospective business development and strategy, then proposed better to downsizing and restructuring, I suggest leaving this company and GM accepted (Still best relationships)</p>

    <div class="role"><span>Business Development| Manager Renza High-Tech (Hong Kong) Limited | Hong Kong</span><span>Aug 2020 – Apr 2021</span></div>
    <p class="text">Start from BD of medical digital devices (Organic disinfection water, see HP: sanitek.example) constructing frameworks for saving COVID-19 pandemic. After the project timeline and to-dos were fixed, received direct offer from president of next company to move on.</p>

    <div class="role"><span>Business Development Manager | Tenfold Global | Hong Kong</span><span>Apr2019 –Mar 2020</span></div>
    <p class="text">Demonstrate mastery in the production of a new TV program with Gulf National News Agency (TV station) for introducing cutting-edge science such as human-type robots; creating program/production budgets and completed all interactions with the research institute on behalf of the TV station and also planned the 12 episodes of the first episode</p>

    <div class="role"><span>Head of Division | Lumen3 Tech Limited(Former QR Consulting, Company name changes) | Hong Kong</span><span>Sep 2018 – Mar 2019</span></div>
    <p class="text">Pioneered a zero-based customized Crypto Exchange platform, overseeing process improvement initiatives and facilitating prompt delivery to clients. Direct staff operations for the total IEO / STO business production, building and maintaining strategic relationships with all levels of stakeholders. Earned 3million HKS in 3 months of working on the BPO’s contract for the establishment of cryptocurrency exchange and new products (token), delivering the product by the deadline and succeeded in restructuring a negative company business into a profit-oriented enterprise. Stellar record of outperforming corporate expectations in meeting goals and objectives while strengthening effective communications with internal stakeholders, vendor and client team members.</p>
    <ul class="list" style="margin-top:3px">
      <li>Participated in high-profile business trip meetings, managed and oversaw daily chat communications as well as prepared and presented operational reports to management and key stakeholders.</li>
      <li>Orchestrate the provision of outstanding oversight for five diverse internal departments and three regions (HK, Philippines and Japan) utilizing multiple business management software and remote work applications including video meetings.</li>
      <li>Exceeded expectations in creating and managing content for movies and documents including white paper writing, Community Management, increasing market positioning, and optimizing revenue growth.</li>
      <li>Appraised for developing and delivering tokens to clients using exceptional customer service management to generate business while facilitating customers’ integration wallet and listing exchange for a casino operator’s ICO project.</li>
      <li>Mastermind the process of instituting infrastructures and external vendor systems such as Customer Due Diligence, and trading systems to the ICO platform.</li>
      <li>Displayed solid leadership abilities in team building / mentoring activities and optimized project branding processes involving HR oversight and staffing as well as financial control for the ICO project.</li>
      <li>Recognized for extensive financial acumen and expertise in budget controls (P&amp;L, BS), generated a record $1.2 M in profit and achieved all ICO requirements while successfully listing one exchange at a time.</li>
      <li>Accomplished in diverse Ad-hoc operations encompassing accounting, payroll management, contract oversight, as well as corporate liaison with vendors, exchanges and other multi-functional professionals involved in project works.</li>
    </ul>
    <p class="note">*As I could not expect any further promotion, I transfer to further develop my career and gain multi-national business acumen.</p>
  </div>

  <footer class="footer"><span>EMIKO TANABE</span>|<span>ETANABE512@MAIL.EXAMPLE</span>|<span>+852 0000 1234/0000 5678</span></footer>
</section>

<!-- Page 3 -->
<section class="page page--three">
  <header class="masthead">
    <p class="masthead__label">CURRICULUM VITAE</p>
    <h1 class="masthead__name">EMIKO TANABE <span class="masthead__city">(Wanchai, Hong Kong)</span></h1>
  </header>

  <div class="body" style="top:56px">
    <div class="role"><span>Senior Manager | QR Consulting International, Hong Kong</span><span>May 2016 –Sep 2018 (Mar 2019)</span></div>
    <p class="text">Outperformed corporate expectations in leading and supervising cryptocurrency white label exchange operations by improving systems that cannot be managed by email / chats, utilizing project management software, solving unexpected issues, and implementing process improvement initiatives and manuals. Adept in managing multiple projects, achieving stable operational exchange, and contributing to end user increase from 1500 to 5000. Reputed for consistent updates to the ever-changing customers’ desired requirements on the platform to achieve strategic goals. Named as Taiwan’s market project leader by the CEO, overseeing a remote team of professionals located in Tokyo, Osaka, Hong Kong, and Europe. Monitored specific project progress and status while also communicating and liaising between client and Fintech Service Vendors (B2B and B2C businesses) to build consensus</p>
    <ul class="list" style="margin-top:3px">
      <li>Played a key role in leading and managing Customer Due Diligence (KYC/KYB) operations including the creation manual to manage risk and prevent financial misconduct for CS (Customer Success)</li>
      <li>Competently developed new tokens and adhered to clients’ requests in establishing an on-time implementation exchange platform to ease the process of exchanging major cryptocurrencies such as leading coins.</li>
      <li>Promptly delivered exchange debit cards linked with the customers’ cryptocurrency wallet while crypto compliance changes.</li>
      <li>Spearheaded global business operations while overseeing the Taiwan subsidiary business expansion set up to encompass crypto-fiat trading, hiring and training staff, deposit/withdrawal operations to Taiwanese partner b2b clients, and bulk trading. Generated 500 initial customers before handover to the local manager.</li>
    </ul>
    <p class="note">*Company name just changed from QR Consulting International Limited to Lumen3 Tech Limited (Same Shareholders)</p>

    <div class="role" style="margin-top:10px"><span>Project Manager | PT. SERAYA BALI | Denpasar</span><span>2014 – 2015</span></div>
    <ul class="list"><li>Strategic planning of corporate projects with B2B institutions at Bali of Indonesia Microfinance and Property Corporate.</li></ul>
    <p class="note">*Relocate to Hong Kong by personal reason at the time late 2015</p>

    <div class="role"><span>Chief Operation Officer | Meridian Agency | Tokyo</span><span>2010 – 2014</span></div>
    <ul class="list"><li>Structured and pioneered the process of running the Tokyo branch of a Singaporean restaurant by connecting with the F&amp;B company. Demonstrated strength in PR including the English Media to increase brand awareness and clientele growth.</li></ul>
    <p class="note">*The business cessation requirements of the JV Agreement are met. (Reason cannot be given due to confidentiality, but I can answer orally.)</p>

    <h2 class="section-title" style="margin-top:14px">CORE COMPETENCIES</h2>
    <div class="competencies">
      <ul><li>Global Operations Management</li><li>Strategic Partnerships</li><li>Process Improvement Champion</li><li>Strategic Planning &amp; Execution</li><li>Cryptocurrency | B2B B2B2C</li><li>Research &amp; Development</li></ul>
      <ul><li>Key Account Management</li><li>Business Restructuring</li><li>Team Leadership / Management</li><li>P &amp; L / Revenue Growth</li><li>Budget Management</li><li>Channel Sales B2B + B2G</li></ul>
      <ul><li>Staff Training / Retention</li><li>Business Administration</li><li>Supply Chain Management</li><li>Vendor / Partner Management</li><li>Negotiations &amp; Agreements</li><li>Records &amp; Documentation</li></ul>
    </div>
  </div>

  <footer class="footer"><span>EMIKO TANABE</span>|<span>ETANABE512@MAIL.EXAMPLE</span>|<span>+852 0000 1234/0000 5678</span></footer>
</section>

</body>
</html>
```